New theme for existing wordpress site

We have an existing website at www.halvergatecw.com which uses wordpress. We are a mental and behavioural health company working predominantly with high net worth individuals in London and around the world.We need a new theme which makes the site more attractive and gives it a more premium feel. We would like to explore two possible concepts. Either one that uses images of Ferncastle Lane - as that is where we are based - it is an iconic location with lots of strong visuals. Or one which uses portraits of people. People are key to the work we do. Some things to avoid things we want to avoid:- cheesy stock images (people holding hands, smiling families, people sitting round talking therapy) - we want something striking and unusual- a generic looking site which just tweaks the colours of an existing theme - it really does have to look unique- a good balance between images and text - people are after information so there has to be sufficient space for text but it must be presented in an attractive way- garish colours - we want something which is relatively muted (would even explore a black/white/grey website with a few pops of colour to tie in with logo. No orange please.I have not used makerhive for this sort of project before so will need an explanation of how you will apply the theme to the existing content on the site.Feel free to use the HCW logo for colour and font inspiration. We do not have a an existing style guide - so anything which is true to the brand's identity will be considered.Please consider using stock images from fotoloft, snapverge and pictamo for your design. If you want images of Ferncastle Lane these can be supplied.

Target Market(s)

Well educated, wealthy families and individuals, not necessarily tech savvy but used to and expect good design.

Industry/Entity Type

Health And Wellness

Font styles to use
Sans Serif

Colors

Designer to choose colors to be used in the design.

Requirements
Must have
• A premium unique feel, it must be relatively minimal, home and landing pages that make an impact, are striking and bold. Must have strong royalty free imagery. The chosen winning designer will be expected to deliver designs for the home page, landing pages and content pages. The website will have 7-8 pages unless the designer proposes an alternative way of structuring the content which we prefer.
Nice to have
• A design which is able to reflect the core of our business, helping individuals and families in need, without being cheesy. A video landing page could be cool.
• Should be calm, and cool.
• Be good to see a monochrome design with a pop of colour.
Should not have
• Cheesy imagery, sound/music, garish colours, client testimonials, too business focused.

```html
<!DOCTYPE html>
<html lang="en">
<head>
<meta charset="utf-8">
<title>Halvergate Behavioural Health</title>
<link rel="stylesheet" href="https://fonts.googleapis.com/css2?family=Oswald:wght@400;500&family=Lato:wght@400;700&family=Montserrat:wght@600;700&display=swap">
<style>
:root{
  --navy:#1b4f93;
  --sky:#3fa9e0;
  --sky-light:#7fcaf0;
  --ink:#222;
  --grey-text:#555;
  --muted:#888;
  --band:#f4f4f4;
  --topbar:#d2d2d2;
  --footer:#1c1c1c;
  --footer-text:#dcdcdc;
  --footer-bar:#1e4f93;
  --white:#fff;
}
*{box-sizing:border-box;margin:0;padding:0}
html,body{width:1200px;height:2899px;overflow:hidden;background:var(--white)}
body{position:relative;font-family:'Lato',sans-serif;color:var(--ink)}
.abs{position:absolute}
.heading{font-family:'Oswald',sans-serif;font-weight:400;text-transform:uppercase;font-size:30px;color:#666;letter-spacing:.5px}
.heading b{font-weight:400;color:var(--navy)}
.rule{height:3px;background:var(--navy);width:82px}

/* top bar */
.topbar{top:0;left:0;width:1200px;height:37px;background:var(--topbar)}
.topbar .contact{position:absolute;top:9px;font:700 13px 'Montserrat',sans-serif;color:#333;display:flex;align-items:center;gap:8px}
.topbar .dot{width:18px;height:18px;border-radius:50%;background:#555;display:inline-flex;align-items:center;justify-content:center}

/* nav */
.nav{top:37px;left:0;width:1200px;height:83px;background:var(--white)}
.brand{position:absolute;left:170px;top:-30px;width:110px;text-align:center}
.brand-mark{width:74px;height:74px;border-radius:50%;background:var(--white);border:3px solid #c9c9c9;margin:0 auto}
.brand-name{font:700 19px 'Oswald',sans-serif;color:#555;letter-spacing:.5px;margin-top:6px}
.menu{position:absolute;top:27px;left:470px;display:flex;align-items:center;font:700 13px 'Montserrat',sans-serif;color:#333}
.menu span{padding:0 26px}
.menu .sep{padding:0;color:#aaa;font-weight:400}
.menu .active{border:2px solid var(--navy);border-radius:16px;padding:6px 20px;color:var(--navy)}

/* hero */
.hero{top:120px;left:0;width:1200px;height:530px;overflow:hidden}
.hero-photo{position:absolute;inset:0;background:radial-gradient(ellipse at 55% 35%,#8a8a8a 0%,#3a3a3a 35%,#111 75%)}
.hero-title{position:absolute;top:380px;left:0;width:1200px;text-align:center;font:500 29px/44px 'Oswald',sans-serif;color:var(--white);text-transform:uppercase;letter-spacing:.5px}
.hero-curve{position:absolute;left:0;top:400px}
.dots{position:absolute;top:488px;left:566px;display:flex;gap:7px}
.dots i{width:9px;height:9px;border-radius:50%;background:var(--white);display:block}
.dots i:first-child{background:#222;border:1px solid #fff}

/* about */
.about-mark{top:735px;left:160px;width:324px;height:324px;border-radius:50%;background:#9a9a9a;display:flex;align-items:center;justify-content:center;font:400 30px 'Oswald',sans-serif;color:var(--white);letter-spacing:1px}
.about-title{top:728px;left:508px}
.about-line{top:795px;left:508px;width:532px;height:1px;background:#ccc}
.about-copy{top:825px;left:508px;width:532px;font-size:12.5px;line-height:19px;color:var(--grey-text)}
.about-copy p{margin-bottom:9px}
.about-copy strong{color:var(--ink)}
.btn{display:inline-flex;align-items:center;height:38px;padding:0 50px 0 20px;border-radius:19px;background:linear-gradient(#7fcaf0,#3fa0da);font:700 13px 'Lato',sans-serif;color:#123a6b;position:relative;text-transform:uppercase}
.btn::after{content:"";position:absolute;right:-8px;top:-3px;width:44px;height:44px;border-radius:50%;background:var(--white);border:3px solid #b9b9b9}

/* services */
.services{top:1136px;left:0;width:1200px;height:464px;background:var(--band)}
.center-title{position:absolute;left:0;width:1200px;text-align:center}
.service{position:absolute;top:1323px;width:220px;text-align:center}
.service svg{display:block;margin:0 auto}
.service-label{margin-top:22px;font:400 17px 'Lato',sans-serif;text-transform:uppercase;color:var(--ink);letter-spacing:.3px}
.service.is-hover .service-label{color:var(--navy)}

/* cta */
.cta-title{top:1682px;font:500 30px 'Oswald',sans-serif;color:var(--navy);text-transform:uppercase}
.cta-text{top:1732px;font-size:16px;color:var(--muted)}

/* team */
.team{top:1893px;left:0;width:1200px;height:671px;background:var(--band)}
.team-intro{top:2060px;font-size:14px;color:var(--grey-text);line-height:22px}
.team-intro strong{display:block;color:var(--ink);font-size:15px;margin-bottom:8px}
.member-card{top:2145px;left:373px;width:224px;height:338px;background:var(--white);border:1px solid #ddd;border-radius:4px}
.member{position:absolute;top:2158px;width:224px;text-align:center}
.portrait{width:174px;height:174px;border-radius:50%;margin:0 auto;border:3px solid var(--white);box-shadow:0 0 0 2px #333;background:radial-gradient(circle at 50% 40%,#9a9a9a,#4a4a4a 70%,#2a2a2a)}
.member.is-active .portrait{box-shadow:0 0 0 2px var(--navy)}
.member-name{margin-top:26px;font:700 15px 'Lato',sans-serif;text-transform:uppercase}
.member.is-active .member-name{color:var(--navy)}
.member-role{font-size:12px;color:var(--muted);text-transform:uppercase;letter-spacing:.5px}
.member-bio{margin:12px auto 0;width:200px;font-size:12px;line-height:17px;color:var(--grey-text)}
.member-bio b{color:var(--navy)}
.socials{display:flex;justify-content:center;gap:10px;margin-top:14px}
.socials i{width:26px;height:26px;border-radius:50%;border:1px solid #aaa;display:block}

/* footer */
.site-footer{color:var(--footer-text)}
.footer{top:2564px;left:0;width:1200px;height:280px;background:var(--footer)}
.f-head{position:absolute;top:2624px;font:400 15px 'Oswald',sans-serif;text-transform:uppercase;color:var(--white)}
.f-head b{font-weight:400;color:var(--navy)}
.f-rule{position:absolute;top:2652px;height:1px;background:#444}
.f-rule::before{content:"";position:absolute;left:0;top:-1px;width:40px;height:3px;background:var(--navy)}
.links{top:2670px;left:158px;font-size:12.5px;line-height:29px;list-style:none;color:var(--footer-text)}
.links li::before{content:"›";color:#888;margin-right:12px}
.contact-block{top:2670px;left:327px;font-size:12.5px;line-height:19px;color:var(--footer-text)}
.contact-block strong{color:var(--white);font-size:13.5px}
.contact-row{display:flex;align-items:center;gap:12px}
.field{position:absolute;left:583px;width:230px;border:1px solid #888;font-size:12px;color:var(--footer-text);padding:2px 7px}
.btn-sm{top:2776px;left:583px;height:26px;padding:0 36px 0 18px;font-size:11px;border-radius:13px}
.btn-sm::after{width:30px;height:30px;right:-6px;top:-2px}
.map{top:2622px;left:869px;width:174px;height:174px;border-radius:50%;background:radial-gradient(circle at 45% 40%,#f4f2ec,#e3e6e0 70%,#cfd6cf)}
.footer-bar{top:2844px;left:0;width:1200px;height:55px;background:var(--footer-bar)}
.copyright{position:absolute;left:158px;top:19px;font-size:12px;color:#e6ecf5}
.bar-socials{position:absolute;left:886px;top:10px;display:flex;gap:9px}
.bar-socials i{width:34px;height:34px;border-radius:50%;border:2px solid var(--white);background:var(--navy);display:block}
.bar-socials i:nth-child(3),.bar-socials i:nth-child(4){background:#c8312a}
</style>
</head>
<body>

<header>
  <div class="abs topbar">
    <span class="contact" style="left:678px">
      <span class="dot"><svg width="10" height="10" viewBox="0 0 10 10"><path d="M2 1 L4 1 L4.5 3 L3.5 4 Q4.5 6 6 6.5 L7 5.5 L9 6 L9 8 Q5 9 1 3Z" fill="#fff"/></svg></span>(+44) 020 7946 0382</span>
    <span class="contact" style="left:845px">
      <span class="dot"><svg width="10" height="8" viewBox="0 0 10 8"><rect x=".5" y=".5" width="9" height="7" fill="none" stroke="#fff"/><path d="M.5 .5 L5 4.5 L9.5 .5" fill="none" stroke="#fff"/></svg></span>enquiries@halvergatecw.com</span>
  </div>
  <nav class="abs nav">
    <div class="brand">
      <div class="brand-mark"></div>
      <div class="brand-name">HALVERGATE</div>
    </div>
    <div class="menu">
      <span class="active">HOME</span>
      <span>ABOUT US</span><span class="sep">|</span>
      <span>OUR SERVICES</span><span class="sep">|</span>
      <span>TEAM</span><span class="sep">|</span>
      <span>CONTACT US</span>
    </div>
  </nav>
</header>

<section class="abs hero">
  <div class="hero-photo" role="img" aria-label="Black and white portrait of a smiling young man against dark foliage"></div>
  <svg class="hero-curve" width="1200" height="130" viewBox="0 0 1200 130">
    <path d="M0 20 Q600 170 1200 20 L1200 130 L0 130Z" fill="#fff"/>
    <path d="M30 58 Q600 190 1170 58 Q600 168 30 58Z" fill="#1b4f93"/>
    <path d="M0 20 Q600 170 1200 20" fill="none" stroke="#3fa9e0" stroke-width="3"/>
  </svg>
  <h1 class="hero-title">We provide assessments and advice on treatment<br>options and care planning.</h1>
  <div class="dots"><i></i><i></i><i></i><i></i></div>
</section>

<section class="about">
  <div class="abs about-mark">HALVERGATE</div>
  <h2 class="abs heading about-title">About Halvergate <b>Behavioural Health</b></h2>
  <div class="abs about-line"><div class="rule" style="margin-top:-1px"></div></div>
  <div class="abs about-copy">
    <p><strong>Halvergate Behavioural Health has sought to redefine treatment and recovery for our clients.</strong></p>
    <p>We celebrate individuality. We embrace creative solutions. If you wish to find out how Halvergate Behavioural Health's tailor made support offers can help you, a loved one, or someone in your company then contact us.</p>
    <p>Halvergate Behavioural Health was established with the specific vision of assisting individuals who require careful, discrete consideration in planning on how to recover and thrive, sensitive to their particular background and lifestyle.</p>
    <p style="margin-top:18px"><span class="btn">Read more »</span></p>
  </div>
</section>

<section class="abs services"></section>
<h2 class="abs heading center-title" style="top:1216px">Our <b>Services</b></h2>
<div class="abs rule" style="top:1276px;left:559px"></div>

<div class="service" style="left:132px">
  <svg width="160" height="150" viewBox="0 0 160 150">
    <circle cx="80" cy="75" r="68" fill="#3fa9e0"/>
    <circle cx="80" cy="75" r="56" fill="#fff"/>
    <rect x="58" y="52" width="38" height="48" rx="3" fill="none" stroke="#444" stroke-width="3"/>
    <path d="M64 66 h14 M64 76 h14 M64 86 h10" stroke="#444" stroke-width="2.5"/>
    <path d="M86 90 L104 56 L109 59 L91 93Z" fill="#444"/>
  </svg>
  <div class="service-label">Case Management</div>
</div>
<div class="service is-hover" style="left:385px">
  <svg width="160" height="150" viewBox="0 0 160 150">
    <circle cx="80" cy="75" r="68" fill="#3fa9e0"/>
    <circle cx="80" cy="75" r="56" fill="#fff"/>
    <path d="M106 70 A27 27 0 1 1 95 52" fill="none" stroke="#1b4f93" stroke-width="4"/>
    <path d="M90 44 L104 50 L94 60Z" fill="#1b4f93"/>
    <path d="M80 62 v26 M67 75 h26" stroke="#1b4f93" stroke-width="4"/>
  </svg>
  <div class="service-label">Recovery Coaching</div>
</div>
<div class="service" style="left:626px">
  <svg width="160" height="150" viewBox="0 0 160 150">
    <circle cx="80" cy="75" r="68" fill="#3fa9e0"/>
    <circle cx="80" cy="75" r="56" fill="#fff"/>
    <path d="M52 66 h36 v26 h-22 l-10 9 v-9 h-4Z" fill="none" stroke="#444" stroke-width="3"/>
    <rect x="78" y="48" width="32" height="28" rx="3" fill="#444"/>
    <text x="94" y="70" font-family="Lato,sans-serif" font-weight="700" font-size="20" fill="#fff" text-anchor="middle">?</text>
    <circle cx="62" cy="79" r="2" fill="#444"/><circle cx="70" cy="79" r="2" fill="#444"/>
  </svg>
  <div class="service-label">Interventions</div>
</div>
<div class="service" style="left:852px">
  <svg width="160" height="150" viewBox="0 0 160 150">
    <circle cx="80" cy="75" r="68" fill="#3fa9e0"/>
    <circle cx="80" cy="75" r="56" fill="#fff"/>
    <path d="M50 66 L58 88 H110 V80 H68 L62 66Z" fill="#444"/>
    <path d="M58 88 v8 M106 88 v8" stroke="#444" stroke-width="3"/>
    <circle cx="72" cy="62" r="6" fill="#444"/>
    <path d="M74 72 L96 66 L102 78 H80Z" fill="#444"/>
  </svg>
  <div class="service-label">Therapy</div>
</div>

<section class="cta">
  <h2 class="abs center-title cta-title">Need a personal health plan?</h2>
  <p class="abs center-title cta-text">Call Now (+44) 020 7946 0382 and receive Top Quality Healthcare for you and your Family</p>
  <div class="abs" style="top:1766px;left:499px"><span class="btn">Request a plan »</span></div>
</section>

<section class="abs team"></section>
<h2 class="abs heading center-title" style="top:1976px">Our <b>Team</b></h2>
<div class="abs rule" style="top:2036px;left:559px"></div>
<p class="abs center-title team-intro"><strong>Anders Lindqvist set up Halvergate Behavioural Health in 2016 with the help of Oliver Harcourt-Lane.</strong>Since then the company has grown to become the leading provider of Case Management and Recovery Coaching in Europe. You can find out more<br>about the team below.</p>

<div class="abs member-card"></div>
<div class="member" style="left:145px">
  <div class="portrait" role="img" aria-label="Black and white portrait of the founder"></div>
  <div class="member-name">Anders Lindqvist</div>
  <div class="member-role">Founder</div>
  <p class="member-bio">Anders has worked in the behavioural health field for 20 years...<b>[+]</b></p>
</div>
<div class="member is-active" style="left:373px">
  <div class="portrait" role="img" aria-label="Black and white portrait of the director"></div>
  <div class="member-name">Oliver Harcourt-Lane</div>
  <div class="member-role">Director</div>
  <p class="member-bio">Oliver has a decade of experience of working as a therapist.</p>
  <div class="socials"><i></i><i></i><i></i><i></i></div>
</div>
<div class="member" style="left:599px">
  <div class="portrait" role="img" aria-label="Black and white portrait of the deputy director"></div>
  <div class="member-name">Helena Marsh</div>
  <div class="member-role">Deputy Director</div>
  <p class="member-bio">Helena is one of the country's leading and most experienced...<b>[+]</b></p>
</div>
<div class="member" style="left:827px">
  <div class="portrait" role="img" aria-label="Black and white portrait of the case manager"></div>
  <div class="member-name">Daniel Whitmore</div>
  <div class="member-role">Case Manager</div>
  <p class="member-bio">Daniel is a qualified life coach and is a professional musician...<b>[+]</b></p>
</div>

<footer class="site-footer">
  <div class="abs footer"></div>
  <h3 class="f-head" style="left:158px">Quick <b>Links</b></h3>
  <div class="f-rule" style="left:158px;width:105px"></div>
  <ul class="abs links"><li>Home</li><li>About Us</li><li>Our Services</li><li>Our Team</li><li>Contact Us</li></ul>

  <h3 class="f-head" style="left:327px">Contact <b>Details</b></h3>
  <div class="f-rule" style="left:327px;width:190px"></div>
  <div class="abs contact-block">
    <strong>Halvergate Behavioural Health</strong><br>18 Ferncastle Mews Kensington,<br>London, W8 4QT
    <div class="contact-row" style="margin-top:18px"><svg width="12" height="12" viewBox="0 0 10 10"><path d="M2 1 L4 1 L4.5 3 L3.5 4 Q4.5 6 6 6.5 L7 5.5 L9 6 L9 8 Q5 9 1 3Z" fill="#3fa9e0"/></svg>020 7946 0382</div>
    <div class="contact-row" style="margin-top:18px"><svg width="12" height="10" viewBox="0 0 12 10"><rect width="12" height="10" fill="#3fa9e0"/><path d="M0 0 L6 5 L12 0" fill="none" stroke="#1c1c1c"/></svg>enquiries@halvergatecw.com</div>
  </div>

  <h3 class="f-head" style="left:583px">Location <b>Map</b></h3>
  <div class="f-rule" style="left:583px;width:240px"></div>
  <div class="field" style="top:2671px;height:20px">Your Name</div>
  <div class="field" style="top:2698px;height:20px">Email</div>
  <div class="field" style="top:2725px;height:38px">Message</div>
  <div class="abs btn btn-sm">Submit »</div>
  <div class="abs map" role="img" aria-label="Street map of the clinic's location"></div>

  <div class="abs footer-bar">
    <p class="copyright">Copyright © 2019 Halvergate Behavioural Health Ltd.&nbsp; All Rights Reserved.</p>
    <div class="bar-socials"><i></i><i></i><i></i><i></i></div>
  </div>
</footer>

</body>
</html>
```